Bright Ledger Path's Mortgage Arc

For BrightLedgerPath.org - Creating a sequence of web pages for consumers to understand their mortgage through Mortgage Arc. There are six pages - want the designer to be willing to design and code those six pages. Most of the pages are very similar.

```html
<!DOCTYPE html>
<html lang="en">
<head>
<meta charset="utf-8">
<title>Bright Ledger Path – Conventional Mortgage</title>
<link rel="stylesheet" href="https://fonts.googleapis.com/css2?family=Catamaran:wght@300;400;600;700&family=Montserrat:wght@400;500&display=swap">
<style>
  :root {
    --top-blue: #1b7fd8;
    --nav-blue: #0a28c8;
    --btn-green: #13c27a;
    --accent-blue: #1230d0;
    --text-dark: #111111;
    --text-mid: #333333;
    --divider: #b8b8b8;
    --panel: #ffffff;
    --footer-blue: #1465d2;
  }
  * { margin: 0; padding: 0; box-sizing: border-box; }
  html, body { width: 1200px; height: 1161px; overflow: hidden; }
  body {
    position: relative;
    font-family: "Catamaran", sans-serif;
    color: var(--text-dark);
    background: linear-gradient(135deg, #e6e6ea 0%, #f4f4f6 35%, #e9e9ec 65%, #f6f6f8 100%);
  }
  .abs { position: absolute; white-space: nowrap; }

  .top-bar { position: absolute; left: 0; top: 0; width: 1200px; height: 50px; background: var(--top-blue); }
  .login-btn {
    position: absolute; left: 509px; top: 7px; width: 74px; height: 35px;
    background: var(--btn-green); border: 1px solid #9ee8c6; color: #fff;
    font: 500 14px/33px "Montserrat", sans-serif; text-align: center;
  }
  .nav-bar { position: absolute; left: 0; top: 50px; width: 1200px; height: 87px; background: var(--nav-blue); }
  .brand { position: absolute; left: 156px; top: 81px; display: flex; align-items: center; gap: 8px; }
  .brand-mark { width: 30px; height: 30px; background: #fff; border-radius: 4px; }
  .brand-name { font: 500 18px/1 "Montserrat", sans-serif; color: #fff; }
  .nav-link { position: absolute; top: 85px; font: 500 13.5px/16px "Montserrat", sans-serif; color: #fff; }

  .page-title { position: absolute; left: 0; width: 1200px; top: 176px; text-align: center; font-weight: 700; font-size: 31px; line-height: 36px; }
  .page-subtitle { position: absolute; left: 0; width: 1200px; top: 224px; text-align: center; font-weight: 300; font-size: 24px; line-height: 28px; color: #222; }

  .proposed { position: absolute; left: 113px; top: 303px; font-size: 24px; line-height: 30px; font-weight: 300; }
  .proposed strong { font-weight: 700; margin-left: 12px; }

  .col-divider { position: absolute; top: 399px; height: 498px; width: 1px; background: var(--divider); }

  .panel { position: absolute; left: 90px; width: 827px; background: var(--panel); box-shadow: 0 2px 6px rgba(0,0,0,0.06); }
  .panel-amount { top: 580px; height: 144px; }
  .panel-total { top: 931px; height: 68px; }
  .panel-divider { position: absolute; width: 1px; background: #cfcfcf; }

  .row-label { position: absolute; left: 113px; font-weight: 600; font-size: 19px; line-height: 22px; }
  .row-label.low { left: 111px; }
  .row-label.accent { color: var(--accent-blue); }
  .row-note { position: absolute; left: 113px; top: 683px; font-size: 14px; line-height: 16px; color: var(--text-mid); }
  .cell { position: absolute; width: 140px; text-align: right; font-weight: 300; font-size: 18px; line-height: 22px; }
  .cell.bold { font-weight: 700; }

  .side-main {
    position: absolute; left: 1005px; top: 161px; width: 137px; height: 86px;
    background: var(--nav-blue); border-radius: 6px; color: #fff;
    font-size: 19px; line-height: 29px; text-align: center; padding-top: 14px;
  }
  .side-btn {
    position: absolute; left: 1005px; width: 137px; height: 86px;
    border: 1px solid var(--accent-blue); border-radius: 6px; color: var(--accent-blue);
    font-size: 18.5px; line-height: 26px; text-align: center;
    display: flex; align-items: center; justify-content: center; background: transparent;
  }
  .payments-box {
    position: absolute; left: 985px; top: 755px; width: 178px; height: 296px;
    background: #fff; text-align: center;
  }
  .payments-box .title { position: absolute; left: 0; width: 178px; top: 23px; font-weight: 700; font-size: 19px; line-height: 29px; }
  .payments-box .item { position: absolute; left: 0; width: 178px; font-weight: 300; font-size: 18px; line-height: 22px; }
  .payments-box .amount { position: absolute; left: 0; width: 178px; font-weight: 700; font-size: 18px; line-height: 22px; }

  .footer { position: absolute; left: 0; top: 1107px; width: 1200px; height: 54px; background: var(--footer-blue); color: #fff; font-family: "Montserrat", sans-serif; }
  .footer .small { position: absolute; top: 20px; font-size: 10px; line-height: 12px; }
  .social-dot { position: absolute; top: 13px; width: 28px; height: 28px; border-radius: 50%; background: #3c5fb4; }
  .page-code { position: absolute; left: 1153px; top: 19px; font-size: 13px; line-height: 16px; }
</style>
</head>
<body>
  <header>
    <div class="top-bar"><div class="login-btn">LOG IN</div></div>
    <div class="nav-bar"></div>
    <div class="brand"><span class="brand-mark"></span><span class="brand-name">BrightLedgerPath</span></div>
    <nav>
      <span class="nav-link" style="left:610px">Home</span>
      <span class="nav-link" style="left:675px">Testimonials</span>
      <span class="nav-link" style="left:784px">Programs</span>
      <span class="nav-link" style="left:875px">FAQ ▾</span>
      <span class="nav-link" style="left:938px">Blog</span>
      <span class="nav-link" style="left:992px">Podcast</span>
    </nav>
  </header>

  <main>
    <h1 class="page-title">Conventional Mortgage</h1>
    <p class="page-subtitle">Mortgage Qualifies</p>
    <p class="proposed">Proposed Payment: <strong>$2,000</strong></p>

    <div class="col-divider" style="left:478px"></div>
    <div class="col-divider" style="left:632px"></div>
    <div class="col-divider" style="left:784px"></div>

    <span class="row-label" style="top:405px">Credit Score</span>
    <span class="cell" style="left:298px;top:402px">707</span>
    <span class="cell" style="left:457px;top:402px">720</span>
    <span class="cell" style="left:610px;top:402px">740</span>
    <span class="cell" style="left:760px;top:402px">760</span>

    <span class="row-label" style="top:456px">Sales Price</span>
    <span class="cell" style="left:298px;top:453px">$250,000</span>
    <span class="cell" style="left:457px;top:453px">$260,000</span>
    <span class="cell" style="left:610px;top:453px">$270,000</span>
    <span class="cell" style="left:760px;top:453px">$280,000</span>

    <span class="row-label" style="top:508px">Down Payment</span>
    <span class="cell" style="left:298px;top:505px">$10,000</span>
    <span class="cell" style="left:457px;top:505px">$10,000</span>
    <span class="cell" style="left:610px;top:505px">$10,000</span>
    <span class="cell" style="left:760px;top:505px">$10,000</span>

    <section class="panel panel-amount">
      <div class="panel-divider" style="left:388px;top:22px;height:102px"></div>
      <div class="panel-divider" style="left:542px;top:22px;height:102px"></div>
      <div class="panel-divider" style="left:694px;top:22px;height:102px"></div>
    </section>
    <span class="row-label accent" style="top:603px">Mortgage Amount</span>
    <span class="cell bold" style="left:297px;top:602px">$240,000</span>
    <span class="cell bold" style="left:459px;top:602px">$250,000</span>
    <span class="cell bold" style="left:610px;top:602px">$260,000</span>
    <span class="cell bold" style="left:754px;top:602px">$270,000</span>

    <span class="row-label accent" style="top:660px">Increase in Purchasing Power</span>
    <span class="row-note">Keeping the payment about the same</span>
    <span class="cell bold" style="left:459px;top:660px">$10,000</span>
    <span class="cell bold" style="left:610px;top:660px">$20,000</span>
    <span class="cell bold" style="left:754px;top:660px">$30,000</span>

    <span class="row-label low" style="top:775px">Interest Rate</span>
    <span class="cell" style="left:298px;top:769px">7.00%</span>
    <span class="cell" style="left:457px;top:769px">6.75%</span>
    <span class="cell" style="left:610px;top:769px">6.50%</span>
    <span class="cell" style="left:760px;top:769px">6.25%</span>

    <span class="row-label low" style="top:822px">Principle &amp; Interest</span>
    <span class="cell" style="left:298px;top:820px">$1,620.23</span>
    <span class="cell" style="left:457px;top:820px">$1630.23</span>
    <span class="cell" style="left:610px;top:820px">$1633.23</span>
    <span class="cell" style="left:760px;top:820px">$1,636.23</span>

    <span class="row-label low" style="top:868px">Mortgage Insurance</span>
    <span class="cell" style="left:298px;top:872px">$113.12</span>
    <span class="cell" style="left:457px;top:872px">$105.12</span>
    <span class="cell" style="left:610px;top:872px">$101.12</span>
    <span class="cell" style="left:760px;top:872px">$101.12</span>

    <section class="panel panel-total"></section>
    <span class="row-label accent low" style="top:954px">Total Payment</span>
    <span class="cell bold" style="left:296px;top:953px">$2,000.15</span>
    <span class="cell bold" style="left:457px;top:953px">$2,001.25</span>
    <span class="cell bold" style="left:610px;top:953px">$2,000.25</span>
    <span class="cell bold" style="left:766px;top:953px">$1,999.92</span>
  </main>

  <aside>
    <div class="side-main">Mortgage<br>Central</div>
    <div class="side-btn" style="top:297px">Edit Mortgage<br>Profile</div>
    <div class="side-btn" style="top:408px">Specific Sales<br>Price</div>
    <div class="side-btn" style="top:519px">Specific<br>Mortgage<br>Payment</div>
    <div class="side-btn" style="top:631px">Maximum<br>Mortgage<br>Qualification</div>
    <div class="payments-box">
      <div class="title">Total Payments<br>Include</div>
      <div class="item" style="top:100px">Property Taxes</div>
      <div class="amount" style="top:143px">$125.00</div>
      <div class="item" style="top:194px">Home Insurance</div>
      <div class="amount" style="top:238px">$125.00</div>
    </div>
  </aside>

  <footer class="footer">
    <span class="small" style="left:153px">Copyright 2023 by Bright Ledger Path</span>
    <span class="social-dot" style="left:555px"></span>
    <span class="social-dot" style="left:587px"></span>
    <span class="social-dot" style="left:619px"></span>
    <span class="small" style="left:873px">Terms Of Use &nbsp;|&nbsp; Privacy Statement</span>
    <span class="page-code">C54</span>
  </footer>
</body>
</html>
```